rhyming dictionary website (easy)

i need a web design for my new website which for now runs on my own self made design (i am a programmer so it sucks) you can find it at http://www.tallow-grove.com

i would like a nicer design that will not cause visitors to flee in disgust.

Target Market(s)

people who search for rhymes, poets, rappers, and normal birthday greeting people

Requirements
Must have
• this is what it needs to have:

1. main page which is simple and must emphasize on the search bar.

2. search result page that will emphasize on the rhyming words and make them clear and important, it also needs to be separable like in the current "design".
it also need to have a good placement of ads, not too intrusive, not too unnoticeable

3. a general page with no real content that i can fill with anything later.
Nice to have
• also the design could combine the already exist logo that you can see on the website, i added it in the uploaded files, along with its psd.

p.s:
other design i liked that you can inspire yourself from
http://www.quillbox.net/RhymingDictionary/hello.html

```html
<!DOCTYPE html>
<html lang="en">
<head>
<meta charset="utf-8">
<title>TallowGrove - Your online source for rhymes</title>
<link rel="stylesheet" href="https://fonts.googleapis.com/css2?family=Roboto+Condensed:ital,wght@0,300;0,400;0,700;1,300;1,400&display=swap">
<style>
  :root {
    --hero-bg: #e8e8e8;
    --ink: #2e2e2e;
    --ink-soft: #3a3a3a;
    --muted: #ababab;
    --band-top: #4a4a4a;
    --band-bottom: #3c3c3c;
    --band-edge: #1f1f1f;
    --link: #6fd0ec;
    --accent: #72c05b;
    --accent-dark: #5a9e46;
    --field-bg: #f5f5f5;
    --field-border: #cfcfcf;
    --placeholder: #b8b8b8;
    --white: #ffffff;
  }
  * { box-sizing: border-box; margin: 0; padding: 0; }
  html, body {
    width: 1200px; height: 812px; overflow: hidden;
    background: var(--white);
    font-family: "Roboto Condensed", "Arial Narrow", sans-serif;
    color: var(--ink);
  }
  .page { position: relative; width: 1200px; height: 812px; }

  .hero {
    position: absolute; left: 0; top: 0; width: 1200px; height: 450px;
    background: var(--hero-bg);
  }
  .brand-mark {
    position: absolute; left: 0; width: 1200px; top: 56px;
    display: flex; justify-content: center; align-items: center; gap: 10px;
    font-size: 26px; font-weight: 700; color: var(--ink);
  }
  .brand-mark .dot { width: 16px; height: 16px; background: var(--accent); }
  .hero-title {
    position: absolute; left: 0; width: 1200px; top: 158px;
    text-align: center; font-size: 46px; font-weight: 300; line-height: 1;
    color: var(--ink);
  }
  .hero-title strong { font-weight: 700; }
  .hero-intro {
    position: absolute; left: 0; width: 1200px; top: 244px;
    text-align: center; font-size: 15.5px; font-weight: 300; line-height: 28px;
    color: var(--ink-soft);
  }
  .search {
    position: absolute; top: 338px; left: 362px;
    display: flex; gap: 16px;
  }
  .search-field {
    width: 334px; height: 50px;
    background: var(--field-bg);
    border: 1px solid var(--field-border); border-radius: 4px;
    box-shadow: inset 0 1px 6px rgba(0,0,0,0.08);
    padding: 0 19px; line-height: 48px;
    font-size: 15px; font-style: italic; color: var(--placeholder);
  }
  .search-button {
    width: 125px; height: 50px;
    background: var(--accent); border: 0; border-radius: 3px;
    box-shadow: 0 3px 0 var(--accent-dark);
    color: var(--white); font-family: inherit; font-weight: 700;
    font-size: 16px; text-transform: uppercase;
    text-shadow: 0 1px 1px rgba(0,0,0,0.3);
  }

  .latest {
    position: absolute; left: 0; top: 450px; width: 1200px; height: 92px;
    background: linear-gradient(var(--band-top), var(--band-bottom));
    border-top: 1px solid var(--band-edge);
    border-bottom: 1px solid var(--band-edge);
    display: flex; align-items: center; padding-left: 189px;
  }
  .latest-label {
    color: var(--white); font-weight: 700; font-size: 16px;
    text-transform: uppercase; margin-right: 28px;
  }
  .latest-list { display: flex; gap: 23px; list-style: none; }
  .latest-list a {
    color: var(--link); font-style: italic; font-size: 16px;
    text-decoration: underline;
  }

  .tagline {
    position: absolute; left: 0; width: 1200px; top: 580px;
    text-align: center; font-size: 17px; font-weight: 300; line-height: 28px;
    color: var(--muted);
  }
  .footer-note {
    position: absolute; left: 0; width: 1200px; top: 715px;
    text-align: center; font-size: 17px; font-weight: 300; line-height: 28px;
    color: var(--ink);
  }
</style>
</head>
<body>
<div class="page">
  <header class="hero">
    <div class="brand-mark"><span class="dot"></span><span>TallowGrove</span></div>
    <h1 class="hero-title"><strong>TallowGrove</strong> - Your online source for rhymes</h1>
    <p class="hero-intro">So you're writing a song or a poem and are frustrated from searching for the right rhyme?<br>Then you're in the right place!</p>
    <form class="search">
      <div class="search-field">What rhymes with.....</div>
      <button class="search-button" type="button">Find out</button>
    </form>
  </header>

  <nav class="latest">
    <span class="latest-label">Latest searches:</span>
    <ul class="latest-list">
      <li><a href="#">Hello</a></li>
      <li><a href="#">Sex</a></li>
      <li><a href="#">Dead</a></li>
      <li><a href="#">more</a></li>
      <li><a href="#">throne</a></li>
    </ul>
  </nav>

  <p class="tagline">Our automated system will fix you the perfect rhyme, that will<br>make you look like the poet you always wanted to be</p>

  <footer class="footer-note">All rights are allright<br>They are reserved as they well deserved.</footer>
</div>
</body>
</html>
```